Modern business card and stationary design for Tech consulting company (startup)
Veromb Technologies Limited
Modern business card and stationary design for Tech consulting company (startup) - Information Technology
Creative Brief
Professional
Malcolm Dewhurst
CEO
Suite 24613 Lower Ground Floor 212-224 Harwell Road London, N7 2QD
mdewhurst@veromb.co.uk
www.veromb.co.uk
Designers, This project is for business card and stationary design. What I’m looking for is design based around the colour scheme of the attached logo. As yet the website is still being designed, but the attached business logo will give you a reference point for the corporate colours. I have attached a couple of links with a general idea of what I’m looking for; http://www.plandoria.com/drafts/display/contest/518230/draft/3047612 http://www.plandoria.com/drafts/display/contest/518230/draft/3048945 All submitted designs will be rated on a regular basis. If you have any further questions relating to this project, please let get in touch. The winning design will be required to provide editable versions of the files (i.e. personal contact details etc.) Good luck

```html
<!DOCTYPE html>
<html lang="en">
<head>
<meta charset="utf-8">
<title>Veromb Technologies – Business Card</title>
<link href="https://fonts.googleapis.com/css2?family=Montserrat:wght@500;700&display=swap" rel="stylesheet">
<style>
  :root {
    --backdrop: #2b2b2d;
    --brand-red: #d2151c;
    --brand-red-deep: #8e0a0f;
    --brand-red-light: #e8333a;
    --card-white: #ffffff;
    --card-shade: #ececec;
    --ink-grey: #6b6b6b;
    --ink-dark: #3a3a3a;
  }
  * { box-sizing: border-box; margin: 0; padding: 0; }
  html, body {
    width: 1200px; height: 901px; overflow: hidden;
    background: var(--backdrop);
    font-family: "Montserrat", Arial, sans-serif;
  }
  .canvas { position: relative; width: 1200px; height: 901px; }

  .card {
    position: absolute;
    width: 640px; height: 366px;
    border-radius: 22px;
    box-shadow: 0 14px 30px rgba(0,0,0,.45);
    overflow: hidden;
  }

  /* Front: red side */
  .card-front {
    left: 80px; top: 70px;
    background: radial-gradient(ellipse at 38% 40%, var(--brand-red-light) 0%, var(--brand-red) 45%, var(--brand-red-deep) 100%);
    display: flex; flex-direction: column; align-items: center; justify-content: center;
    gap: 26px;
  }
  .front-brand { display: flex; align-items: center; gap: 18px; }
  .front-brand .brand-square { width: 44px; height: 44px; background: var(--card-white); }
  .front-brand .brand-name {
    color: var(--card-white); font-weight: 700; font-size: 46px; letter-spacing: 8px;
  }
  .front-web {
    color: var(--card-white); font-weight: 500; font-size: 14px; letter-spacing: 5px;
  }

  /* Back: white side */
  .card-back {
    left: 480px; top: 465px;
    background: linear-gradient(160deg, var(--card-white) 60%, var(--card-shade) 100%);
  }
  .holder {
    position: absolute; right: 34px; top: 34px;
    font-size: 15px; letter-spacing: 1px; color: var(--brand-red); font-weight: 500;
  }
  .holder .role { color: var(--ink-grey); font-size: 11px; }
  .holder .divider { color: var(--ink-grey); margin: 0 6px; }

  .back-brand {
    position: absolute; left: 30px; top: 172px;
    width: 300px;
    display: flex; align-items: center; gap: 10px;
  }
  .back-brand .brand-square { width: 24px; height: 24px; background: var(--brand-red); flex: none; }
  .back-brand .brand-name {
    color: var(--brand-red); font-weight: 700; font-size: 15px; letter-spacing: 1.5px;
    white-space: nowrap;
  }

  .contact {
    position: absolute; left: 360px; top: 118px;
    font-size: 11px; line-height: 15px; letter-spacing: .6px;
    color: var(--ink-dark); text-transform: uppercase;
  }
  .contact .address { margin-bottom: 6px; }
  .contact .row { display: flex; align-items: center; gap: 8px; height: 16px; }
  .contact svg { width: 12px; height: 12px; flex: none; fill: var(--brand-red); }
</style>
</head>
<body>
<div class="canvas">

  <section class="card card-front">
    <div class="front-brand">
      <span class="brand-square"></span>
      <span class="brand-name">VEROMB</span>
    </div>
    <div class="front-web">WWW.VEROMB.CO.UK</div>
  </section>

  <section class="card card-back">
    <p class="holder">MALCOLM DEWHURST<span class="divider">|</span><span class="role">CEO</span></p>

    <div class="back-brand">
      <span class="brand-square"></span>
      <span class="brand-name">VEROMB TECHNOLOGIES</span>
    </div>

    <div class="contact">
      <p class="address">Suite 24613<br>Lower Ground Floor<br>212-224 Harwell Road<br>London, N7 2QD</p>
      <p class="row">
        <svg viewBox="0 0 24 24" aria-hidden="true"><path d="M6.6 10.8a15.2 15.2 0 0 0 6.6 6.6l2.2-2.2a1 1 0 0 1 1-.25 11.4 11.4 0 0 0 3.6.57 1 1 0 0 1 1 1V20a1 1 0 0 1-1 1A17 17 0 0 1 3 4a1 1 0 0 1 1-1h3.5a1 1 0 0 1 1 1c0 1.25.2 2.45.57 3.6a1 1 0 0 1-.25 1z"/></svg>
        +44 (0)845 7391024
      </p>
      <p class="row">
        <svg viewBox="0 0 24 24" aria-hidden="true"><path d="M7 1h10a2 2 0 0 1 2 2v18a2 2 0 0 1-2 2H7a2 2 0 0 1-2-2V3a2 2 0 0 1 2-2zm0 3v14h10V4zm5 15.5a1.2 1.2 0 1 0 0 2.4 1.2 1.2 0 0 0 0-2.4z"/></svg>
        +44 (0)7814 530296
      </p>
      <p class="row">
        <svg viewBox="0 0 24 24" aria-hidden="true"><path d="M2 5h20v14H2zm2 2v.4l8 5 8-5V7zm0 2.8V17h16V9.8l-8 5z"/></svg>
        mdewhurst@veromb.co.uk
      </p>
      <p class="row">
        <svg viewBox="0 0 24 24" aria-hidden="true"><path d="M12 2a10 10 0 1 0 0 20 10 10 0 0 0 0-20zm6.9 6h-3a15 15 0 0 0-1.4-3.9A8 8 0 0 1 18.9 8zM12 4c.8 1.2 1.5 2.5 1.9 4h-3.8c.4-1.5 1.1-2.800 1.9-4zM4.3 14a8 8 0 0 1 0-4h3.4a16 16 0 0 0 0 4zm.8 2h3a15 15 0 0 0 1.4 3.9A8 8 0 0 1 5.1 16zm3-8h-3a8 8 0 0 1 4.4-3.9A15 15 0 0 0 8.1 8zM12 20c-.8-1.2-1.5-2.5-1.9-4h3.8c-.4 1.5-1.1 2.8-1.9 4zm2.3-6H9.7a14 14 0 0 1 0-4h4.6a14 14 0 0 1 0 4zm.2 5.9a15 15 0 0 0 1.4-3.9h3a8 8 0 0 1-4.4 3.9zm1.8-5.9a16 16 0 0 0 0-4h3.4a8 8 0 0 1 0 4z"/></svg>
        www.veromb.co.uk
      </p>
    </div>
  </section>

</div>
</body>
</html>
```